real esate business card with company logo and name

we need a business card design for a real esate company

The company name is Walsh & Ortiz Pty Ltd, and we have our logo designed and will upload. We want classic or moden feel. Black or white background. looks more textured. Should include folowinginformations
Paul Walsh and Tara Ortiz
Sales Agents & Onsite Manager
p: 07 5948 2610
F: 07 5948 2795
M:0451 786 923
3/22 Marlow Crescent, ELLEN GROVE QLD 4078

We want this business card looks professonal. Thank you in advance.

Industry/Entity Type

Real Estate Agent

Contact Information for Business Card

Paul Walsh and Tara Ortiz
Onsite Manager & Sales Agents
p: 07 5948 2610
M:0451 786 923

Font styles to use
Serif

Colors
000000
fbfbfb
333333
959595

Requirements
Must have
• company logo and name, black or white back ground

```html
<!DOCTYPE html>
<html lang="en">
<head>
<meta charset="utf-8">
<title>Walsh &amp; Ortiz Pty Ltd – Business Card</title>
<link rel="stylesheet" href="https://fonts.googleapis.com/css2?family=Cinzel:wght@500&family=Cormorant+Garamond:ital,wght@1,400&family=Della+Respira&display=swap">
<style>
  :root {
    --card-black: #000000;
    --card-surface-light: #242424;
    --card-surface-dark: #121212;
    --ink-white: #fbfbfb;
    --ink-soft: #d6d6d6;
    --ink-grey: #959595;
    --rule-grey: #333333;
    --rule-mid: #5a5a5a;
  }
  * { margin: 0; padding: 0; box-sizing: border-box; }
  html, body {
    width: 1200px;
    height: 686px;
    overflow: hidden;
    background: var(--card-black);
  }
  .business-card {
    position: relative;
    width: 1200px;
    height: 686px;
    overflow: hidden;
    background: radial-gradient(ellipse at 40% 35%, var(--card-surface-light) 0%, var(--card-surface-dark) 75%);
    color: var(--ink-white);
  }
  .agent-names {
    position: absolute;
    left: 80px;
    top: 40px;
    font-family: "Cinzel", serif;
    font-weight: 500;
    font-size: 35px;
    letter-spacing: 0.5px;
    color: var(--ink-white);
    white-space: nowrap;
  }
  .agent-roles {
    position: absolute;
    left: 80px;
    top: 90px;
    font-family: "Cormorant Garamond", serif;
    font-style: italic;
    font-size: 38px;
    letter-spacing: 0.3px;
    color: var(--ink-grey);
    white-space: nowrap;
  }
  .brand-mark {
    position: absolute;
    left: 110px;
    top: 232px;
    width: 236px;
    height: 236px;
    background: var(--rule-grey);
  }
  .brand-name {
    position: absolute;
    left: 80px;
    top: 512px;
    font-family: "Della Respira", serif;
    font-size: 32px;
    color: var(--ink-grey);
    white-space: nowrap;
  }
  .contact-list {
    position: absolute;
    left: 612px;
    top: 262px;
    list-style: none;
    font-family: "Della Respira", serif;
    font-size: 35px;
    color: var(--ink-white);
  }
  .contact-item {
    display: flex;
    align-items: flex-start;
    margin-bottom: 30px;
    line-height: 44px;
  }
  .contact-icon {
    width: 26px;
    height: 44px;
    margin-right: 33px;
    flex: none;
  }
  .contact-icon svg { display: block; width: 26px; height: 44px; fill: var(--ink-soft); }
  .contact-address { line-height: 47px; }
  .base-rule {
    position: absolute;
    left: 0;
    top: 619px;
    width: 1122px;
    height: 9px;
  }
</style>
</head>
<body>
  <main class="business-card">
    <h1 class="agent-names">Paul Walsh and Tara Ortiz</h1>
    <p class="agent-roles">Onsite Manager &amp; Sales Agents</p>

    <div class="brand-mark" aria-hidden="true"></div>
    <p class="brand-name">Walsh &amp; Ortiz Pty Ltd</p>

    <ul class="contact-list">
      <li class="contact-item">
        <span class="contact-icon" aria-label="Phone">
          <svg viewBox="0 0 26 44"><path d="M6 10c2-1 4-1 5 1l2 5c.5 1.5-.5 2.5-2 3l-1 .5c1 3 3 6 5.5 8l1-.8c1.2-1 2.6-.8 3.4.5l3 4.2c.8 1.4.2 2.8-1.5 3.6-2.2 1-4.6.5-6.6-1.2C9 28.8 5.5 22 4.2 15.5 3.7 13 4.3 11 6 10z"/></svg>
        </span>
        <span>07 5948 2610</span>
      </li>
      <li class="contact-item">
        <span class="contact-icon" aria-label="Mobile">
          <svg viewBox="0 0 26 44"><path d="M5 8h16a2 2 0 0 1 2 2v26a2 2 0 0 1-2 2H5a2 2 0 0 1-2-2V10a2 2 0 0 1 2-2zm1 4v20h14V12zm7 21.5a1.5 1.5 0 1 0 0 3 1.5 1.5 0 0 0 0-3z"/></svg>
        </span>
        <span>0451 786 923</span>
      </li>
      <li class="contact-item">
        <span class="contact-icon" aria-label="Address">
          <svg viewBox="0 0 26 44"><path d="M13 8a9 9 0 0 1 9 9c0 6-9 17-9 17S4 23 4 17a9 9 0 0 1 9-9zm0 5.5a3.5 3.5 0 1 0 0 7 3.5 3.5 0 0 0 0-7z"/></svg>
        </span>
        <span class="contact-address">3/22 Marlow Crescent<br>ASHBURY VALE QLD 4086</span>
      </li>
    </ul>

    <svg class="base-rule" viewBox="0 0 1122 9" preserveAspectRatio="none" aria-hidden="true">
      <polygon points="0,0 1122,0 1114,9 0,9" fill="var(--rule-mid)"/>
    </svg>
  </main>
</body>
</html>
```